Professional Modern Website Design

We are a premium IT services provider to the financial industry based in London. Our company is called Veltra our current holding page is www.veltra-example.co.uk. We require a new website to match our new corporate identity. This project is for the design phase only. Development will be handled in-house. I have attached examples of wire frames we have developed (although open to suggestions for improvement) Our brand document that should demonstrate current brand, inc how we communicate to potential clients and finally mostly completed web-content.
We are looking for designers that can create something that sets us apart from our competitors.
Target Market(s)
IT Decision makers in Finance companies such as; hedge funds, private investment banks etc
Industry/Entity Type
Financial
Number of Pages Required
5+ page
Requirements
Must have
- hexagon elements in the design, unique design.
Nice to have
- Blog and social media feeds
Should not have
- Should not resemble a downloaded template

```html
<!DOCTYPE html>
<html lang="en">
<head>
<meta charset="utf-8">
<title>Veltra</title>
<link href="https://fonts.googleapis.com/css2?family=Open+Sans:wght@400;600;700&family=Roboto+Condensed:wght@400&display=swap" rel="stylesheet">
<style>
:root{
  --orange:#f7941d;
  --black:#0b0b0b;
  --dark:#1c1c1c;
  --footer:#262626;
  --bottom:#3b3b3b;
  --text:#333;
  --muted:#555;
  --white:#fff;
}
*{box-sizing:border-box;margin:0;padding:0}
html,body{width:772px;height:1200px;overflow:hidden}
body{font-family:"Open Sans",sans-serif;background:var(--white);color:var(--text);position:relative}
.site-header{position:absolute;left:0;top:0;width:772px;height:67px;background:var(--black)}
.brand{position:absolute;left:56px;top:18px;display:flex;align-items:center;gap:8px;color:var(--white);font-weight:700;font-size:17px;letter-spacing:2px}
.brand-square{width:22px;height:22px;background:var(--orange)}
.header-tools{position:absolute;right:52px;top:22px;display:flex;align-items:center;gap:14px}
.divider{width:1px;height:22px;background:#777}
.social-dot{width:16px;height:16px;border-radius:50%;background:var(--white)}
.main-nav{position:absolute;left:0;top:67px;width:772px;height:30px;background:var(--orange);padding-left:56px;display:flex}
.main-nav a{color:var(--white);text-decoration:none;font-size:11.5px;line-height:30px;padding:0 8px}
.main-nav a.active{background:var(--black)}
.hero{position:absolute;left:0;top:97px;width:772px;height:383px;background:linear-gradient(120deg,#d9d6d0 0%,#efece6 40%,#c9a47a 65%,#e4ddd2 100%)}
.hero-card{position:absolute;left:56px;top:156px;width:235px;height:196px;background:var(--dark);padding:14px 12px;color:var(--white)}
.hero-card h1{font-family:"Roboto Condensed",sans-serif;font-weight:400;font-size:14px;line-height:21px;white-space:nowrap}
.hero-card hr{border:0;border-top:1px solid var(--orange);margin:9px 0 10px}
.hero-card p{font-size:8.5px;line-height:14px;color:#ddd}
.btn-orange{display:inline-block;margin-top:16px;background:var(--orange);color:var(--white);font-size:8.5px;padding:5px 16px;border:1px solid #fff3}
.slider-dots{position:absolute;left:368px;top:356px;display:flex;gap:3px}
.slider-dots span{width:7px;height:7px;background:var(--black)}
.slider-dots span.on{background:var(--orange)}
.intro{position:absolute;left:0;top:515px;width:772px;text-align:center}
.intro h2{font-weight:400;font-size:22px;color:#222}
.intro p{margin:14px auto 0;width:460px;font-size:11px;line-height:18px;color:var(--muted)}
.roles{position:absolute;left:56px;top:627px;display:flex;gap:20px}
.role{width:150px;text-align:center}
.role svg{display:block;width:150px;height:173px}
.role h3{margin:14px -10px 0;font-size:11px;line-height:15px;font-weight:600;letter-spacing:.4px;color:#222;white-space:nowrap}
.role .rule{margin:6px auto 0;width:106px;border-top:2px dotted var(--orange)}
.role p{margin-top:7px;font-size:8.5px;line-height:13.5px;color:var(--muted)}
.btn-outline{display:inline-block;margin-top:12px;width:64px;height:18px;line-height:16px;border:1px solid var(--orange);color:var(--orange);font-size:7.5px}
.site-footer{position:absolute;left:0;top:975px;width:772px;height:185px;background:var(--footer);color:var(--white)}
.foot-col{position:absolute;top:31px;font-size:8px;line-height:12px}
.foot-col h4{font-size:8.5px;font-weight:600;margin-bottom:12px}
.foot-col p{margin-bottom:11px}
.foot-links li{list-style:none;display:flex;align-items:center;gap:8px;margin-bottom:6px}
.foot-links svg{width:9px;height:7px}
.foot-brand{position:absolute;left:547px;top:0;width:66px;height:98px;background:var(--white);display:flex;flex-direction:column;align-items:center;justify-content:center;gap:8px;color:var(--muted);font-size:10px;font-weight:600;letter-spacing:1.5px}
.foot-brand .brand-square{width:30px;height:30px}
.foot-social{position:absolute;left:624px;top:45px;display:flex;gap:13px}
.bottom-bar{position:absolute;left:0;top:1160px;width:772px;height:40px;background:var(--bottom);color:var(--white);font-size:8px;text-align:center;line-height:40px}
</style>
</head>
<body>
<header class="site-header">
  <div class="brand"><span class="brand-square"></span>VELTRA</div>
  <div class="header-tools">
    <svg width="16" height="16" viewBox="0 0 16 16" aria-label="Search"><circle cx="6.5" cy="6.5" r="4.5" fill="none" stroke="#fff" stroke-width="2"/><line x1="10" y1="10" x2="14.5" y2="14.5" stroke="#fff" stroke-width="2"/></svg>
    <span class="divider"></span>
    <span class="social-dot"></span><span class="social-dot"></span><span class="social-dot"></span><span class="social-dot"></span>
  </div>
</header>
<nav class="main-nav">
  <a class="active">Home</a><a>About</a><a>Services</a><a>Partners</a><a>Clients</a><a>Contact</a>
</nav>
<section class="hero" role="img" aria-label="Photograph of stacked coins on financial documents">
  <div class="hero-card">
    <h1>You Need Integration. We're<br>Invisible but Always Supporting You..</h1>
    <hr>
    <p>Veltra is One of the Leading systems integrators to the world's finance Sector. We are an Extension of your Business and Our Services Portfolio has been built so you have access to a Complete Partner.</p>
    <span class="btn-orange">About Us</span>
  </div>
  <div class="slider-dots"><span class="on"></span><span></span><span></span><span></span></div>
</section>
<section class="intro">
  <h2>WHO ARE YOU?</h2>
  <p>If you're Working in a Financial Organisation, We have the Services to help Everyone in Your Organisation Work More Efficiently, Productively and Profitable.</p>
</section>
<section class="roles">
  <div class="role">
    <svg viewBox="0 0 150 173" role="img" aria-label="Photograph of glasses resting on financial charts"><defs><linearGradient id="g1" x1="0" y1="0" x2="1" y2="1"><stop offset="0" stop-color="#dfe3e8"/><stop offset="1" stop-color="#8d96a0"/></linearGradient></defs><polygon points="75,0 150,43 150,130 75,173 0,130 0,43" fill="var(--orange)"/><polygon points="75,14 138,50 138,123 75,159 12,123 12,50" fill="url(#g1)"/></svg>
    <h3>HEDGEFUND PARTNER/CEO</h3><div class="rule"></div>
    <p>Lorem ipsum dolor sit amet, consectetur adipiscing elit. In gravida rhoncus urna a luctus. Cras vitae libero ut mauris hendrerit interdum.</p>
    <span class="btn-outline">READ MORE</span>
  </div>
  <div class="role">
    <svg viewBox="0 0 150 173" role="img" aria-label="Photograph of coins on a newspaper"><defs><linearGradient id="g2" x1="0" y1="0" x2="1" y2="1"><stop offset="0" stop-color="#e6e6e6"/><stop offset="1" stop-color="#b88a5c"/></linearGradient></defs><polygon points="75,0 150,43 150,130 75,173 0,130 0,43" fill="var(--orange)"/><polygon points="75,14 138,50 138,123 75,159 12,123 12,50" fill="url(#g2)"/></svg>
    <h3>CFO</h3><div class="rule"></div>
    <p>Lorem ipsum dolor sit amet, consectetur adipiscing elit. In gravida rhoncus urna a luctus. Cras vitae libero ut mauris hendrerit interdum.</p>
    <span class="btn-outline">READ MORE</span>
  </div>
  <div class="role">
    <svg viewBox="0 0 150 173" role="img" aria-label="Photograph of a businessman reviewing plans at a desk"><defs><linearGradient id="g3" x1="0" y1="0" x2="1" y2="1"><stop offset="0" stop-color="#cfd3d6"/><stop offset="1" stop-color="#5e6366"/></linearGradient></defs><polygon points="75,0 150,43 150,130 75,173 0,130 0,43" fill="var(--orange)"/><polygon points="75,14 138,50 138,123 75,159 12,123 12,50" fill="url(#g3)"/></svg>
    <h3>CTO</h3><div class="rule"></div>
    <p>Lorem ipsum dolor sit amet, consectetur adipiscing elit. In gravida rhoncus urna a luctus. Cras vitae libero ut mauris hendrerit interdum.</p>
    <span class="btn-outline">READ MORE</span>
  </div>
  <div class="role">
    <svg viewBox="0 0 150 173" role="img" aria-label="Photograph of colleagues in an office meeting"><defs><linearGradient id="g4" x1="0" y1="0" x2="1" y2="1"><stop offset="0" stop-color="#f0f0f0"/><stop offset="1" stop-color="#4a4f57"/></linearGradient></defs><polygon points="75,0 150,43 150,130 75,173 0,130 0,43" fill="var(--orange)"/><polygon points="75,14 138,50 138,123 75,159 12,123 12,50" fill="url(#g4)"/></svg>
    <h3>EMPLOYEE</h3><div class="rule"></div>
    <p>Lorem ipsum dolor sit amet, consectetur adipiscing elit. In gravida rhoncus urna a luctus. Cras vitae libero ut mauris hendrerit interdum.</p>
    <span class="btn-outline">READ MORE</span>
  </div>
</section>
<footer class="site-footer">
  <div class="foot-col" style="left:57px">
    <h4>SITE LINKS</h4>
    <ul class="foot-links">
      <li><svg viewBox="0 0 9 7"><path d="M0 3.5h8M5 0.5l3 3-3 3" fill="none" stroke="#fff"/></svg>Home</li>
      <li><svg viewBox="0 0 9 7"><path d="M0 3.5h8M5 0.5l3 3-3 3" fill="none" stroke="#fff"/></svg>About</li>
      <li><svg viewBox="0 0 9 7"><path d="M0 3.5h8M5 0.5l3 3-3 3" fill="none" stroke="#fff"/></svg>Services</li>
      <li><svg viewBox="0 0 9 7"><path d="M0 3.5h8M5 0.5l3 3-3 3" fill="none" stroke="#fff"/></svg>Partners</li>
      <li><svg viewBox="0 0 9 7"><path d="M0 3.5h8M5 0.5l3 3-3 3" fill="none" stroke="#fff"/></svg>Clients</li>
      <li><svg viewBox="0 0 9 7"><path d="M0 3.5h8M5 0.5l3 3-3 3" fill="none" stroke="#fff"/></svg>Contact</li>
    </ul>
  </div>
  <div class="foot-col" style="left:141px">
    <h4>SUPPORT</h4><p>+44 20 7946 0101</p>
    <h4 style="margin-top:14px">SALES</h4><p>+44 20 7946 0102</p>
  </div>
  <div class="foot-col" style="left:243px">
    <h4>LONDON OFFICE</h4>
    <p>18 HARROW LANE, WESTMERE,<br>LONDON W9Z 4QX</p>
    <p>+44 20 7946 0103</p>
    <p>INFO@VELTRA-EXAMPLE.CO.UK</p>
  </div>
  <div class="foot-col" style="left:380px">
    <h4>ESSEX OFFICE</h4>
    <p>7 ABBOT YARD, MILLBROOK<br>AVENUE, ESSEX SS9 2TR</p>
    <p>+44 20 7946 0101</p>
    <p>INFO@VELTRA-EXAMPLE.CO.UK</p>
  </div>
  <div class="foot-brand"><span class="brand-square"></span>VELTRA</div>
  <div class="foot-social"><span class="social-dot"></span><span class="social-dot"></span><span class="social-dot"></span><span class="social-dot"></span></div>
</footer>
<div class="bottom-bar">© Veltra Limited - Company Registration No. 0000000; Incorporated in England and Wales</div>
</body>
</html>
```